Marrowgate Auctions Business Cards Design Needed

I need a business card design that is modern looking - double sided (maybe just my logo on the back, but open to suggestions) - the overall design is up to you. I want it to be easy to read - not over the top flashy. I already have a company logo which I uploaded so that needs to be used. The colors of my logo are the colors I want on the card... so blue and gray (do need to match the logo colors).

Requirements
Must have
• Would like the card to be sleek, modern and easy to ready

```html
<!DOCTYPE html>
<html lang="en">
<head>
<meta charset="utf-8">
<title>Marrowgate Auctions – Business Cards</title>
<link href="https://fonts.googleapis.com/css2?family=Tinos:wght@400;700&display=swap" rel="stylesheet">
<style>
  :root {
    --stage: #1d1d1d;
    --blue-deep: #2158a6;
    --blue-light: #3aa9d3;
    --logo-blue: #2a72b8;
    --logo-gray: #4a4a4d;
    --white: #ffffff;
    --paper: #ffffff;
  }
  * { margin: 0; padding: 0; box-sizing: border-box; }
  html, body {
    width: 1200px; height: 1200px; overflow: hidden;
    background: var(--stage);
    font-family: "Tinos", "Times New Roman", serif;
  }
  .sheet {
    width: 1200px; height: 1200px;
    display: flex; flex-direction: column; align-items: center; justify-content: center;
    gap: 60px;
  }
  .card {
    width: 700px; height: 400px; position: relative; overflow: hidden;
  }
  /* Front */
  .card--front {
    background: linear-gradient(155deg, var(--blue-deep) 0%, #2f82c0 45%, var(--blue-light) 80%);
    color: var(--white);
  }
  .identity {
    position: absolute; left: 48px; top: 44px;
    display: flex; align-items: flex-start; gap: 16px;
  }
  .identity__square {
    width: 58px; height: 58px; background: rgba(255,255,255,0.18); margin-top: 4px;
  }
  .company { font-weight: 700; font-size: 30px; line-height: 1.1; }
  .person { margin-top: 12px; font-weight: 700; font-size: 21px; }
  .role { font-size: 15px; margin-top: 2px; }
  .tagline {
    position: absolute; left: 60px; bottom: 40px;
    font-size: 24px; line-height: 1.25;
  }
  .contacts {
    position: absolute; right: 0; bottom: 66px;
    list-style: none; display: flex; flex-direction: column; gap: 10px; align-items: flex-end;
  }
  .contact { display: flex; align-items: center; gap: 8px; font-size: 20px; }
  .contact__bar {
    width: 100px; height: 26px; background: var(--white);
    border-radius: 13px 0 0 13px; display: flex; align-items: center; padding-left: 4px;
  }
  .contact__icon {
    width: 20px; height: 20px; border-radius: 50%;
    border: 1.5px solid var(--blue-light);
    display: flex; align-items: center; justify-content: center;
    color: var(--blue-light); font-size: 13px; font-family: Arial, sans-serif;
  }
  /* Back */
  .card--back {
    background: var(--paper);
    display: flex; align-items: center; justify-content: center; gap: 20px;
  }
  .back__square { width: 56px; height: 56px; background: var(--logo-blue); }
  .back__name {
    font-weight: 700; font-size: 54px; color: var(--logo-blue); letter-spacing: 0.5px;
  }
</style>
</head>
<body>
<main class="sheet">
  <section class="card card--front">
    <div class="identity">
      <div class="identity__square"></div>
      <div>
        <div class="company">Marrowgate Auctions, Inc.</div>
        <div class="person">Dana Whitfield</div>
        <div class="role">Owner/President - Auctioneer</div>
      </div>
    </div>
    <ul class="contacts">
      <li class="contact">auctionrevival.com
        <span class="contact__bar"><span class="contact__icon"></span></span></li>
      <li class="contact">info@marrowgateauctions.com
        <span class="contact__bar"><span class="contact__icon">@</span></span></li>
      <li class="contact">555-014-2867
        <span class="contact__bar"><span class="contact__icon">
          <svg width="12" height="12" viewBox="0 0 24 24" aria-hidden="true"><path fill="#3aa9d3" d="M6.6 10.8a15 15 0 0 0 6.6 6.6l2.2-2.2c.3-.3.7-.4 1-.2 1.1.4 2.3.6 3.6.6.6 0 1 .4 1 1V20c0 .6-.4 1-1 1A17 17 0 0 1 3 4c0-.6.4-1 1-1h3.5c.6 0 1 .4 1 1 0 1.3.2 2.5.6 3.6.1.3 0 .7-.2 1z"/></svg>
        </span></span></li>
    </ul>
    <p class="tagline">Improving Charity<br>Auctions Nationwide</p>
  </section>
  <section class="card card--back">
    <div class="back__square"></div>
    <div class="back__name">Marrowgate Auctions</div>
  </section>
</main>
</body>
</html>
```